Fun Location App for users to earn rewards and vouchers everywhere they go

Jorvix is a social app where users can collect rewards when they travel + complete quests at different location to get rewards.

We would like a design of an app that has these features/function
1) Login/Signup Page
2) HomePage - A Map with your current location
- Show the location/stores aroudn
- Have a bag tab to press and get rewards
3) Quests Tab = show all the available tasks
4) Exchange Tab = all the items available for exchange vouchers and can click to know more
5) Wallet Tab = user profile + vouchers in their wallet
6) Partners Tab = Showcase all the partners and can click to know more
7) Claim functions

We have attached a visual example. Do feel free to change what is best fit too. We do need to exact measurements as well to create the app

Target Market(s)

Fun, people who like rewards and interact with friends

Font styles to use
Sans Serif

Colors
f78f20
fbed22
fbee3e

Requirements
Must have
• Yellow, fun interactive feeling.
Nice to have
• Pop up when click on things
Should not have
• nil

```html
<!DOCTYPE html>
<html lang="en">
<head>
<meta charset="utf-8">
<title>Jorvix – App Screens</title>
<link href="https://fonts.googleapis.com/css2?family=Quicksand:wght@400;500;600;700&display=swap" rel="stylesheet">
<style>
  :root{
    --orange:#f78f20;
    --orange-deep:#f59a0c;
    --yellow:#fbc81a;
    --yellow-bright:#fbed22;
    --yellow-soft:#fbee3e;
    --white:#ffffff;
    --ink:#333333;
    --ink-soft:#555555;
    --muted:#8a8a8a;
    --field-grey:#ececec;
    --page:#e3e3e3;
    --panel:#f1f1f1;
    --map:#2c2c2c;
  }
  *{box-sizing:border-box;margin:0;padding:0}
  html,body{width:1200px;height:569px;overflow:hidden}
  body{background:var(--page);font-family:"Quicksand",sans-serif;position:relative;color:var(--ink)}

  .screen{position:absolute;top:41px;width:253px;height:484px;overflow:hidden;background:var(--white)}
  .screen--login{left:60px}
  .screen--signup{left:338px}
  .screen--map{left:626px}
  .screen--quests{left:894px;background:var(--panel)}

  .auth-bg{position:absolute;inset:0;background:linear-gradient(180deg,var(--orange-deep) 30%,var(--yellow) 100%)}
  .auth-head{position:absolute;left:0;top:0;width:253px;height:170px}
  .brand-stack{position:absolute;left:0;right:0;top:30px;text-align:center}
  .brand-stack .brand-dot{display:block;margin:0 auto 4px;width:46px;height:46px;border-radius:50%;background:var(--yellow)}
  .brand-stack .brand-name{font-weight:700;font-size:42px;line-height:1;color:var(--yellow)}
  .screen-title{position:absolute;left:0;right:0;text-align:center;color:var(--white);font-weight:700;font-size:24px}

  .field{position:absolute;height:32px;border-radius:16px;background:var(--white);display:flex;align-items:center;font-size:10px;color:var(--ink-soft);padding-left:14px;overflow:hidden}
  .field--split{padding-left:0}
  .field__label{width:54px;height:100%;background:var(--field-grey);display:flex;align-items:center;justify-content:center;color:var(--muted);font-size:10px;font-weight:600}
  .field__value{padding-left:8px;font-weight:600;color:var(--ink);display:flex;align-items:center;gap:6px}
  .field__chip{position:absolute;right:8px;top:7px;height:18px;padding:0 9px;border-radius:9px;background:var(--yellow-bright);color:var(--orange);font-size:8px;font-weight:700;line-height:18px}
  .field__caret{position:absolute;right:12px;top:11px}

  .btn{position:absolute;height:32px;border-radius:16px;display:flex;align-items:center;justify-content:center;font-weight:700;font-size:12px;letter-spacing:.2px}
  .btn--dark{background:var(--ink);color:var(--white)}
  .btn--outline{border:2px solid var(--white);color:var(--white)}
  .or{position:absolute;left:0;right:0;text-align:center;color:var(--white);font-weight:700;font-size:11px}

  .app-head{position:absolute;left:0;top:0;width:253px;height:66px;z-index:2}
  .brand-row{position:absolute;left:50px;top:12px;display:flex;align-items:center;gap:6px}
  .brand-row .brand-dot{width:22px;height:22px;border-radius:50%;background:var(--yellow)}
  .brand-row .brand-name{font-weight:700;font-size:29px;line-height:1;color:var(--yellow)}
  .gear{position:absolute;right:18px;top:20px}

  .map-area{position:absolute;left:0;top:48px;width:253px;height:392px;background:radial-gradient(circle at 50% 45%,#3a3a3a 0%,var(--map) 55%,#1f1f1f 100%)}
  .pin{position:absolute}
  .here{position:absolute;left:121px;top:224px;width:20px;height:20px;border-radius:50%;background:rgba(247,143,32,.55);display:flex;align-items:center;justify-content:center}
  .here::after{content:"";width:9px;height:9px;border-radius:50%;background:var(--yellow-bright)}

  .bag-card{position:absolute;left:38px;top:376px;width:176px;height:44px;background:var(--white);border:2px solid var(--orange);border-radius:3px;text-align:center;font-size:9px;font-weight:700;padding-top:23px;color:var(--ink)}
  .bag-btn{position:absolute;left:50px;top:364px;width:153px;height:26px;border-radius:13px;background:var(--orange);color:var(--white);font-weight:700;font-size:11px;display:flex;align-items:center;justify-content:center}

  .tab-bar{position:absolute;left:0;bottom:0;width:253px;height:44px;background:linear-gradient(180deg,var(--orange-deep),var(--yellow));display:flex;align-items:center;justify-content:space-around;padding:0 14px}

  .quest-title{position:absolute;left:0;right:0;top:74px;text-align:center;font-weight:700;font-size:20px;color:var(--ink)}
  .quest-sub{position:absolute;left:0;right:0;top:99px;text-align:center;font-size:13px;font-weight:500;color:var(--ink)}
  .quest-card{position:absolute;left:21px;width:213px;height:81px;background:var(--white);display:flex}
  .quest-card__photo{width:104px;height:100%}
  .quest-card__body{padding:14px 0 0 12px;font-size:10px;font-weight:500;line-height:1.35}
  .quest-card__name{font-weight:700;font-size:11px}
  .quest-card__btn{margin-top:8px;width:70px;height:18px;border-radius:9px;background:var(--yellow);color:var(--white);font-weight:700;font-size:8px;display:flex;align-items:center;justify-content:center}
  .chev{position:absolute;left:117px;top:403px}
</style>
</head>
<body>

<svg width="0" height="0" style="position:absolute">
  <defs>
    <symbol id="i-grid" viewBox="0 0 24 20"><rect x="1" y="1" width="9" height="8" fill="#fff"/><rect x="13" y="1" width="9" height="8" fill="none" stroke="#fff" stroke-width="1.5"/><rect x="1" y="11" width="9" height="8" fill="none" stroke="#fff" stroke-width="1.5"/><rect x="13" y="11" width="9" height="8" fill="none" stroke="#fff" stroke-width="1.5"/></symbol>
    <symbol id="i-user" viewBox="0 0 26 26"><circle cx="13" cy="13" r="12" fill="none" stroke="#fff" stroke-width="1.6"/><circle cx="13" cy="10" r="4.5" fill="none" stroke="#fff" stroke-width="1.6"/><path d="M5 21c2-4 5-5.5 8-5.5s6 1.5 8 5.5" fill="none" stroke="#fff" stroke-width="1.6"/></symbol>
    <symbol id="i-pin" viewBox="0 0 20 26"><path d="M10 1C5 1 1 5 1 10c0 7 9 15 9 15s9-8 9-15c0-5-4-9-9-9z" fill="#fff"/><circle cx="10" cy="10" r="3.5" fill="#f9a818"/></symbol>
    <symbol id="i-mappin" viewBox="0 0 24 32"><path d="M12 0C5.4 0 0 5.4 0 12c0 9 12 20 12 20s12-11 12-20C24 5.4 18.6 0 12 0z" fill="#fbd01c"/><circle cx="12" cy="12" r="6.5" fill="#2c2c2c"/></symbol>
  </defs>
</svg>

<section class="screen screen--login">
  <div class="auth-bg"></div>
  <svg class="auth-head" viewBox="0 0 253 170"><path d="M0 0H253V144C214 150 170 138 126 138C82 138 40 158 0 152Z" fill="#fff"/></svg>
  <div class="brand-stack"><span class="brand-dot"></span><span class="brand-name">Jorvix</span></div>
  <h1 class="screen-title" style="top:172px">Log In</h1>
  <div class="field field--split" style="left:21px;top:218px;width:212px">
    <span class="field__label">Mobile</span>
    <span class="field__value">
      <svg width="9" height="15" viewBox="0 0 9 15"><rect x=".7" y=".7" width="7.6" height="13.6" rx="1.5" fill="none" stroke="#f78f20" stroke-width="1.2"/><line x1="3" y1="12" x2="6" y2="12" stroke="#f78f20"/></svg>
      (+65) 90001234</span>
  </div>
  <div class="field field--split" style="left:21px;top:259px;width:212px">
    <span class="field__label">OTP</span>
    <span class="field__value">Input Code</span>
    <span class="field__chip">Get Code</span>
  </div>
  <div class="btn btn--dark" style="left:24px;top:305px;width:211px">LOGIN</div>
  <div class="or" style="top:347px">or</div>
  <div class="btn btn--outline" style="left:22px;top:369px;width:211px;height:33px">SIGN UP</div>
</section>

<section class="screen screen--signup">
  <div class="auth-bg"></div>
  <svg class="auth-head" viewBox="0 0 253 170"><path d="M0 0H253V144C214 150 170 138 126 138C82 138 40 158 0 152Z" fill="#fff"/></svg>
  <div class="brand-stack" style="top:35px"><span class="brand-dot"></span><span class="brand-name">Jorvix</span></div>
  <h1 class="screen-title" style="top:176px">Sign Up</h1>
  <div class="field" style="left:17px;top:217px;width:106px;height:29px">First Name</div>
  <div class="field" style="left:129px;top:217px;width:107px;height:29px">Last Name</div>
  <div class="field" style="left:17px;top:255px;width:221px;height:31px">Username</div>
  <div class="field" style="left:18px;top:294px;width:222px;height:31px">
    <svg width="10" height="10" viewBox="0 0 10 10" style="margin-right:4px"><rect x=".5" y="1.5" width="9" height="8" fill="none" stroke="#fbc81a"/><rect x=".5" y="1.5" width="9" height="2.5" fill="#fbc81a"/></svg>Date of Birth</div>
  <div class="field" style="left:18px;top:331px;width:222px;height:31px">Email</div>
  <div class="field" style="left:20px;top:368px;width:107px;height:30px">Refferral code</div>
  <div class="field" style="left:133px;top:368px;width:107px;height:30px">Select Gender
    <svg class="field__caret" width="9" height="6" viewBox="0 0 9 6"><path d="M1 1l3.5 3.5L8 1" fill="none" stroke="#888" stroke-width="1.2"/></svg></div>
  <div class="btn btn--outline" style="left:24px;top:415px;width:212px;height:33px;font-size:13px;gap:6px">NEXT
    <svg width="7" height="11" viewBox="0 0 7 11"><path d="M1 1l4.5 4.5L1 10" fill="none" stroke="#fff" stroke-width="1.8"/></svg></div>
</section>

<section class="screen screen--map">
  <div class="map-area" role="img" aria-label="Dark street map of the surrounding area"></div>
  <svg class="app-head" viewBox="0 0 253 66"><path d="M0 0H253V52C210 58 170 62 126 60C82 58 40 50 0 56Z" fill="#fff"/></svg>
  <div class="brand-row" style="z-index:3"><span class="brand-dot"></span><span class="brand-name">Jorvix</span></div>
  <svg class="gear" width="18" height="18" viewBox="0 0 24 24" style="z-index:3"><circle cx="12" cy="12" r="3.5" fill="none" stroke="#fbc81a" stroke-width="1.6"/><path d="M12 2l2 3 3.5-1 .5 3.5 3 2-2 3 2 3-3 2-.5 3.5-3.5-1-2 3-2-3-3.5 1-.5-3.5-3-2 2-3-2-3 3-2 .5-3.5 3.5 1z" fill="none" stroke="#fbc81a" stroke-width="1.4"/></svg>
  <svg class="pin" style="left:98px;top:84px" width="19" height="25"><use href="#i-mappin"/></svg>
  <svg class="pin" style="left:187px;top:152px" width="19" height="25"><use href="#i-mappin"/></svg>
  <svg class="pin" style="left:38px;top:172px" width="30" height="40"><use href="#i-mappin"/></svg>
  <svg class="pin" style="left:165px;top:264px" width="20" height="27"><use href="#i-mappin"/></svg>
  <svg class="pin" style="left:33px;top:300px" width="18" height="24"><use href="#i-mappin"/></svg>
  <div class="here"></div>
  <div class="bag-card">5000 x jorcoins &nbsp;|&nbsp; 5 x voucher</div>
  <div class="bag-btn">OPEN YOUR BAG</div>
  <nav class="tab-bar">
    <svg width="22" height="19"><use href="#i-grid"/></svg>
    <svg width="24" height="24"><use href="#i-user"/></svg>
    <svg width="18" height="24"><use href="#i-pin"/></svg>
    <svg width="22" height="19"><use href="#i-grid"/></svg>
    <svg width="24" height="24"><use href="#i-user"/></svg>
  </nav>
</section>

<section class="screen screen--quests">
  <svg class="app-head" viewBox="0 0 253 66"><path d="M0 0H253V52C210 58 170 62 126 60C82 58 40 50 0 56Z" fill="#fff"/></svg>
  <div class="brand-row" style="z-index:3"><span class="brand-dot"></span><span class="brand-name">Jorvix</span></div>
  <svg class="gear" width="18" height="18" viewBox="0 0 24 24" style="z-index:3"><circle cx="12" cy="12" r="3.5" fill="none" stroke="#fbc81a" stroke-width="1.6"/><path d="M12 2l2 3 3.5-1 .5 3.5 3 2-2 3 2 3-3 2-.5 3.5-3.5-1-2 3-2-3-3.5 1-.5-3.5-3-2 2-3-2-3 3-2 .5-3.5 3.5 1z" fill="none" stroke="#fbc81a" stroke-width="1.4"/></svg>
  <h2 class="quest-title">Quest Time!</h2>
  <p class="quest-sub">Challenge to earn rewards</p>

  <article class="quest-card" style="top:127px">
    <div class="quest-card__photo" role="img" aria-label="Photo of a coffee bar interior" style="background:linear-gradient(160deg,#d8d4cc,#6b5a48 70%,#3b2e24)"></div>
    <div class="quest-card__body"><div class="quest-card__name">Cobble Row</div>$1 off any item<div class="quest-card__btn">Challenge</div></div>
  </article>
  <article class="quest-card" style="top:219px">
    <div class="quest-card__photo" role="img" aria-label="Photo of a warmly lit restaurant terrace" style="background:linear-gradient(160deg,#8a3a2a,#c56a3a 45%,#3f6a6a)"></div>
    <div class="quest-card__body"><div class="quest-card__name">Cobble Row</div>$1 off any item<div class="quest-card__btn">Challenge</div></div>
  </article>
  <article class="quest-card" style="top:310px">
    <div class="quest-card__photo" role="img" aria-label="Photo of a street café front" style="background:linear-gradient(160deg,#c9b79a,#8d6a45 55%,#4c3a2a)"></div>
    <div class="quest-card__body" style="padding-top:12px;line-height:1.2"><div class="quest-card__name">Tamsin cafe</div>1 for 1 main dish<br>for dinner<div class="quest-card__btn" style="margin-top:6px">Challenge</div></div>
  </article>
  <svg class="chev" width="19" height="11" viewBox="0 0 19 11"><path d="M1 1l8.5 8.5L18 1" fill="none" stroke="#666" stroke-width="2"/></svg>

  <nav class="tab-bar">
    <svg width="22" height="19"><use href="#i-grid"/></svg>
    <svg width="24" height="24"><use href="#i-user"/></svg>
    <svg width="18" height="24"><use href="#i-pin"/></svg>
    <svg width="22" height="19"><use href="#i-grid"/></svg>
    <svg width="24" height="24"><use href="#i-user"/></svg>
  </nav>
</section>

</body>
</html>
```